KORBALT

The business want a professional looking business card. We have a scetch we will add but want the extra upgrade, and would like more suggestions for variations of our business cards.

```html
<!DOCTYPE html>
<html lang="en">
<head>
<meta charset="utf-8">
<title>KORBALT Business Card</title>
<link href="https://fonts.googleapis.com/css2?family=Marcellus&family=Montserrat:wght@400;700&display=swap" rel="stylesheet">
<style>
  :root {
    --backdrop: #1c1c1e;
    --card: #0e0e0f;
    --gold: #d2ad5c;
    --white: #f1f1f1;
    --pattern-dark: #0b0b0c;
    --pattern-light: #5a5a5e;
  }
  * { margin: 0; padding: 0; box-sizing: border-box; }
  html, body { width: 900px; height: 1200px; overflow: hidden; }
  body { background: var(--backdrop); position: relative; font-family: "Montserrat", sans-serif; }

  .card {
    position: absolute;
    left: 135px;
    width: 630px;
    height: 357px;
    border-radius: 14px;
    background: var(--card);
    overflow: hidden;
  }
  .card--front { top: 216px; }
  .card--back { top: 630px; }

  .front-pattern {
    position: absolute; inset: 0;
    background: linear-gradient(90deg, var(--pattern-dark) 0%, #161618 45%, var(--pattern-light) 100%);
  }
  .front-brand {
    position: absolute;
    left: 0; right: 0; top: 150px;
    text-align: center;
  }
  .brand-name {
    font-family: "Marcellus", serif;
    color: var(--gold);
    font-size: 40px;
    letter-spacing: 14px;
    line-height: 1;
    padding-left: 14px;
    display: block;
  }
  .brand-since {
    display: block;
    font-family: "Montserrat", sans-serif;
    color: var(--gold);
    font-size: 12px;
    letter-spacing: 8px;
    padding-left: 8px;
    margin-top: 16px;
  }

  .holder { position: absolute; left: 51px; top: 58px; }
  .holder-company {
    font-family: "Marcellus", serif;
    color: var(--gold);
    font-size: 29px;
    line-height: 1;
  }
  .holder-role {
    color: var(--white);
    font-size: 22px;
    margin-top: 14px;
    letter-spacing: 1px;
  }
  .holder-name {
    color: var(--gold);
    font-size: 21px;
    font-weight: 700;
    margin-top: 6px;
    letter-spacing: 1px;
  }

  .contact { position: absolute; left: 51px; top: 213px; list-style: none; }
  .contact li {
    display: flex; align-items: center; gap: 6px;
    color: var(--white);
    font-size: 18px;
    letter-spacing: 1.5px;
    height: 29.5px;
  }
  .contact svg { width: 12px; height: 12px; flex: none; }

  .back-brand {
    position: absolute;
    left: 370px; width: 212px; top: 108px;
    text-align: center;
  }
  .back-brand .brand-mark {
    width: 44px; height: 44px; border-radius: 50%;
    background: var(--gold);
    margin: 0 auto 26px;
  }
  .back-brand .brand-name { font-size: 28px; letter-spacing: 10px; padding-left: 10px; }
  .back-brand .brand-since { font-size: 10px; letter-spacing: 5px; margin-top: 8px; padding-left: 5px; }
</style>
</head>
<body>
  <section class="card card--front">
    <div class="front-pattern" role="img" aria-label="Embossed repeating floral ornament pattern, fading from black to silver"></div>
    <div class="front-brand">
      <span class="brand-name">KORBALT</span>
      <span class="brand-since">SINCE 2026</span>
    </div>
  </section>

  <section class="card card--back">
    <div class="holder">
      <p class="holder-company">KORBALT HALVORSEN</p>
      <p class="holder-role">CEO &amp; Founder</p>
      <p class="holder-name">Lars Erik Halvorsen</p>
    </div>
    <ul class="contact">
      <li>
        <svg viewBox="0 0 12 12"><rect x="3" y="1" width="6" height="10" rx="1" fill="none" stroke="var(--gold)" stroke-width="1.2"/><circle cx="6" cy="9.2" r="0.7" fill="var(--gold)"/></svg>
        004791234567
      </li>
      <li>
        <svg viewBox="0 0 12 12"><rect x="1" y="3" width="10" height="7" fill="var(--gold)"/><path d="M1 3 L6 7 L11 3" fill="none" stroke="var(--card)" stroke-width="1"/></svg>
        korbalt.llc@mailbox.com
      </li>
      <li>
        <svg viewBox="0 0 12 12"><circle cx="6" cy="6" r="4.8" fill="none" stroke="var(--gold)" stroke-width="1"/><ellipse cx="6" cy="6" rx="2" ry="4.8" fill="none" stroke="var(--gold)" stroke-width="0.8"/><path d="M1.2 6 H10.8 M2 3.5 H10 M2 8.5 H10" stroke="var(--gold)" stroke-width="0.8"/></svg>
        www.korbalt.llc
      </li>
    </ul>
    <div class="back-brand">
      <div class="brand-mark"></div>
      <span class="brand-name">KORBALT</span>
      <span class="brand-since">SINCE 2026</span>
    </div>
  </section>
</body>
</html>
```